KIT & BO’S FAREWELL TO GNAT BITES

I require an attractive appealing label with the dimensions 7.5m x 3.5cm
This is a Natural sandfly insect repellent cream formulated by 2 pharmacists Carla Penrose and Tom Whitcombe. It is required for labelling a 50 g jar

Contains Essential Oils of cedar wood, rosemary, cinnamon, citronella, lavender, eucalyptus and clove in a moisturising base.

We would like to see designs using the colour bright duck egg blue as the main colour with dark brown tones for the patterns. An eye catching label is output aim . However any colour combination that is attractive to the eye is welcome
A gloss finish is preferable.
Updates

More designs please

Target Market(s)

Trekkers, outdoor active people, pharmacy, health shops

Colors
abd037
34a6d7
0456a4
33b8a4

Requirements
Must have
• Kit and Bo’s
• Farewell to Gnat bites
• Natural Sandfly Repellent
• Contains Essential Oils of cedar wood, rosemary, cinnamon, citronella, lavender, eucalyptus and clove in a moisturising base.
• Formulated by Australian Pharmacists Carla Penrose and Tom Whitcombe
• Made in Australia
• 0462735190
Nice to have
• Sandfly/ flies
• I have attached a label I use for my mozzie cream and would like a similar font please

```html
<!DOCTYPE html>
<html lang="en">
<head>
<meta charset="utf-8">
<title>Kit &amp; Bo’s Farewell to Gnat Bites – Label</title>
<link href="https://fonts.googleapis.com/css2?family=Bellefair&family=Playfair+Display:wght@400&display=swap" rel="stylesheet">
<style>
  :root{
    --white:#ffffff;
    --brown:#7a5a50;
    --duck-egg:#8fdff5;
    --duck-egg-deep:#84d6ee;
    --info-blue:#90e3f9;
    --teal:#1db5b9;
    --teal-light:#3fd0cf;
    --title-teal:#2cc1c4;
  }
  html,body{margin:0;padding:0;width:1200px;height:1200px;overflow:hidden;background:var(--white);}
  .canvas{position:relative;width:1200px;height:1200px;overflow:hidden;background:var(--white);}
  .water-backdrop{position:absolute;left:600px;top:0;width:600px;height:1200px;
    background:linear-gradient(160deg,var(--teal-light) 0%,var(--teal) 45%,#17a9ad 100%);}
  .label{position:absolute;top:24px;width:430px;height:1148px;box-sizing:border-box;
    background:var(--white);border:1.5px solid var(--brown);border-radius:72px;}
  .label--plain{left:80px;}
  .label--teal{left:697px;}
  .label__pattern{position:absolute;left:8px;top:9px;right:8px;bottom:8px;border-radius:62px;
    background:linear-gradient(180deg,var(--duck-egg) 0%,var(--duck-egg-deep) 50%,var(--duck-egg) 100%);
    border:1px solid rgba(122,90,80,.35);}
  .label__brand{position:absolute;left:52px;top:130px;width:324px;height:80px;
    display:flex;align-items:center;justify-content:center;
    font-family:"Bellefair",serif;font-size:58px;color:var(--brown);line-height:1;}
  .label__title{position:absolute;left:40px;top:216px;width:350px;height:198px;margin:0;border-radius:3px;
    display:flex;flex-direction:column;align-items:center;justify-content:center;
    font-family:"Playfair Display",serif;font-weight:400;font-size:66px;line-height:1.2;
    white-space:nowrap;color:var(--white);-webkit-text-stroke:1.2px var(--brown);}
  .label--plain .label__title{background:var(--white);}
  .label--teal .label__title{background:var(--title-teal);}
  .label__claims{position:absolute;left:30px;top:460px;width:370px;
    font-family:"Bellefair",serif;color:var(--brown);text-align:center;}
  .claims__kind{margin:0 0 22px;font-size:30px;line-height:34px;}
  .claims__pharmacists{margin:0 0 22px;font-size:22px;line-height:27px;}
  .claims__origin{margin:0 0 8px;font-size:24px;line-height:28px;}
  .claims__phone{margin:0;font-size:24px;line-height:28px;}
  .label__info{position:absolute;left:20px;top:756px;width:390px;height:306px;box-sizing:border-box;
    background:var(--info-blue);border:1px solid var(--brown);
    font-family:"Bellefair",serif;color:var(--brown);font-size:21px;line-height:23.5px;
    text-align:center;padding-top:10px;}
  .info__maker{margin:0 0 20px;}
  .info__ingredients{margin:0 0 20px;padding:0 8px;}
  .info__field{text-align:left;margin:0 0 13px 22px;font-size:22px;}
</style>
</head>
<body>
<main class="canvas">
  <div class="water-backdrop" role="img" aria-label="Turquoise water surface backdrop"></div>

  <section class="label label--plain">
    <div class="label__pattern" role="img" aria-label="Repeating pattern of small brown sandflies on duck egg blue"></div>
    <div class="label__brand">Kit &amp; Bo’s</div>
    <h1 class="label__title"><span>Farewell to</span><span>Gnat bites</span></h1>
    <div class="label__claims">
      <p class="claims__kind">Natural Sandfly Repellent</p>
      <p class="claims__pharmacists">Formulated by Australian Pharmacists<br>Carla Penrose and Tom Whitcombe</p>
      <p class="claims__origin">Made in Australia</p>
      <p class="claims__phone">0462735190</p>
    </div>
    <div class="label__info">
      <p class="info__maker">Manufactured by:<br>Tom Whitcombe Organic<br>12 Wattle Lane Ballarat Vic<br>(03)59146023</p>
      <p class="info__ingredients">Contains Essential Oils of cedar wood, rosemary, cinnamon, citronella, lavender, eucalyptus and clove in a moisturising base.</p>
      <p class="info__field">Batch No:</p>
      <p class="info__field">Expiry:</p>
    </div>
  </section>

  <section class="label label--teal">
    <div class="label__pattern" role="img" aria-label="Repeating pattern of small brown sandflies on duck egg blue"></div>
    <div class="label__brand">Kit &amp; Bo’s</div>
    <h2 class="label__title"><span>Farewell to</span><span>Gnat bites</span></h2>
    <div class="label__claims">
      <p class="claims__kind">Natural Sandfly Repellent</p>
      <p class="claims__pharmacists">Formulated by Australian Pharmacists<br>Carla Penrose and Tom Whitcombe</p>
      <p class="claims__origin">Made in Australia</p>
      <p class="claims__phone">0462735190</p>
    </div>
    <div class="label__info">
      <p class="info__maker">Manufactured by:<br>Tom Whitcombe Organic<br>12 Wattle Lane Ballarat Vic<br>(03)59146023</p>
      <p class="info__ingredients">Contains Essential Oils of cedar wood, rosemary, cinnamon, citronella, lavender, eucalyptus and clove in a moisturising base.</p>
      <p class="info__field">Batch No:</p>
      <p class="info__field">Expiry:</p>
    </div>
  </section>
</main>
</body>
</html>
```